Valtora

Standard Business Card design.
Sample two-sided design uploaded. White front, Black back.
Would like white shield to be on all black background side.
Willing to look at a couple creative designs, but nothing crazy.
Preference for a classic, confident, strong design.

```html
<!DOCTYPE html>
<html lang="en">
<head>
<meta charset="utf-8">
<title>Valtora Business Card</title>
<link href="https://fonts.googleapis.com/css2?family=Montserrat:wght@700&family=Crimson+Text:wght@400&display=swap" rel="stylesheet">
<style>
  :root {
    --page: #e9e7e3;
    --card-black: #050505;
    --card-white: #ffffff;
    --ink: #1a1a1a;
    --ink-soft: #4a4a4a;
    --rule: #6e6e6e;
    --paper-shade: #f1f1f1;
    --ghost-dark: #101010;
    --ghost-light: #efefef;
  }
  * { margin: 0; padding: 0; box-sizing: border-box; }
  html, body {
    width: 1200px; height: 900px; overflow: hidden;
    background: var(--page);
  }
  .canvas { position: relative; width: 1200px; height: 900px; }
  .card {
    position: absolute; left: 320px;
    width: 560px; height: 320px;
    border-radius: 28px;
    box-shadow: 0 10px 24px rgba(0,0,0,0.18);
    overflow: hidden;
  }
  .card--back { top: 90px; background: var(--card-black); }
  .card--front {
    top: 490px;
    background: linear-gradient(120deg, var(--card-white) 55%, var(--paper-shade));
  }
  .ghost-mark {
    position: absolute; border-radius: 50%;
  }
  .card--back .ghost-mark {
    left: 10px; top: 50px; width: 230px; height: 230px;
    background: var(--ghost-dark);
  }
  .card--front .ghost-mark {
    right: 60px; top: -20px; width: 220px; height: 220px;
    background: var(--ghost-light);
  }
  .brand-square { position: absolute; }
  .card--back .brand-square {
    left: 340px; top: 62px; width: 76px; height: 76px;
    background: var(--card-white);
  }
  .card--front .brand-square {
    left: 74px; top: 26px; width: 48px; height: 48px;
    background: var(--ink);
  }
  .wordmark {
    position: absolute;
    font-family: "Montserrat", sans-serif;
    font-weight: 700;
    letter-spacing: 0.12em;
    line-height: 1;
  }
  .card--back .wordmark {
    left: 262px; top: 160px;
    font-size: 44px; color: var(--card-white);
  }
  .rule { position: absolute; height: 1px; background: var(--rule); }
  .rule--back { left: 266px; width: 250px; top: 222px; background: var(--card-white); }
  .card--front .wordmark {
    left: 40px; top: 86px;
    font-size: 28px; color: var(--ink);
  }
  .rule--brand { left: 40px; width: 150px; top: 124px; }
  .address {
    position: absolute; right: 40px; top: 96px;
    text-align: right;
    font-family: "Crimson Text", serif;
    font-size: 16px; line-height: 1.15; color: var(--ink-soft);
  }
  .person-name {
    position: absolute; left: 40px; top: 142px;
    font-family: "Montserrat", sans-serif; font-weight: 700;
    font-size: 20px; line-height: 1; color: var(--ink-soft);
  }
  .rule--name { left: 206px; right: 40px; top: 152px; }
  .person-role {
    position: absolute; left: 40px; top: 166px;
    font-family: "Crimson Text", serif;
    font-size: 17px; line-height: 1.2; color: var(--ink);
  }
  .rule--role { left: 112px; width: 150px; top: 180px; }
  .contacts {
    position: absolute; left: 40px; top: 206px;
    list-style: none;
    font-family: "Crimson Text", serif;
    font-size: 17px; color: var(--ink-soft);
  }
  .contacts li { display: flex; align-items: center; gap: 10px; height: 26px; }
  .contacts svg { width: 15px; height: 15px; fill: none; stroke: var(--ink); stroke-width: 1.6; }
</style>
</head>
<body>
<main class="canvas">
  <section class="card card--back" aria-label="Card back">
    <div class="ghost-mark" role="img" aria-label="Faint brand mark decoration"></div>
    <div class="brand-square" aria-hidden="true"></div>
    <div class="wordmark">VALTORA</div>
    <div class="rule rule--back"></div>
  </section>

  <section class="card card--front" aria-label="Card front">
    <div class="ghost-mark" role="img" aria-label="Faint brand mark decoration"></div>
    <div class="brand-square" aria-hidden="true"></div>
    <div class="wordmark">VALTORA</div>
    <div class="rule rule--brand"></div>
    <p class="address">00 dummy city<br>place 0000</p>
    <div class="person-name">MARCUS HALE</div>
    <div class="rule rule--name"></div>
    <div class="person-role">Director</div>
    <div class="rule rule--role"></div>
    <ul class="contacts">
      <li>
        <svg viewBox="0 0 16 16" aria-hidden="true"><path d="M3 2l3 0 1 3-2 1.5c1 2 2.5 3.5 4.5 4.5L11 9l3 1v3c-6 1-12-5-11-11z" fill="#1a1a1a" stroke="none"/></svg>
        555-014-2876
      </li>
      <li>
        <svg viewBox="0 0 16 16" aria-hidden="true"><rect x="1.5" y="3.5" width="13" height="9"/><path d="M1.5 3.5L8 9l6.5-5.5"/></svg>
        info@valtora.com
      </li>
      <li>
        <svg viewBox="0 0 16 16" aria-hidden="true"><circle cx="8" cy="8" r="6.5"/><ellipse cx="8" cy="8" rx="3" ry="6.5"/><path d="M1.5 8h13M3 4.5h10M3 11.5h10"/></svg>
        www.valtora.com
      </li>
    </ul>
  </section>
</main>
</body>
</html>
```